Website design for dressage horse training business

Looking to develop a new website design for a dressage horse training website. We want to change from a single landing page to one with multiple pages.
You are free to use your creativity to design the main landing page. This is the only page you need to design at this point. I would encourage looking at other Dressage Training websites to get a feel for what is typically on them. A few websites are listed below although I think the design of them could be better.
Notes:
- Menu to include: Home, Services, News Room, Blog, About Us, Contact,
- FAQ section on main page
- Logo to remain the same - the logo attached is not the correct color so change to match existing color.
- Change 'Sponsors' to 'Partnerships' on main page
Here is the link to the current site:
https://lindenridgestables.com/
Example sites
https://www.crestwoodsporthorsesco.com/
https://corinnalavelledressage.com/
Target Market(s)
Older women with disposable income
Number of Pages Required
1 page
Look and feel
Each slider illustrates characteristics of the customer's brand and the style your logo design should communicate.

```html
<!DOCTYPE html>
<html lang="en">
<head>
<meta charset="utf-8">
<title>Linden Ridge Stables — Dressage &amp; Sport Horse Training</title>
<link rel="stylesheet" href="https://fonts.googleapis.com/css2?family=Playfair+Display:wght@400;700&family=Jost:wght@300;400;500&display=swap">
<style>
:root{
  --gold:#b5854f;
  --gold-soft:#c9a57a;
  --ink:#2e2e2e;
  --text:#5a5a5a;
  --light:#f5f5f5;
  --white:#ffffff;
  --wood:#3a2a21;
}
*{box-sizing:border-box;margin:0;padding:0}
html,body{width:1200px;height:4038px;overflow:hidden}
body{position:relative;background:var(--white);font-family:'Jost',sans-serif;color:var(--text)}
.abs{position:absolute}

/* header */
.hero-bg{position:absolute;left:0;top:0;width:1200px;height:660px}
.brand{position:absolute;left:163px;top:24px;font-family:'Playfair Display',serif;font-weight:400;color:var(--gold);font-size:27px;letter-spacing:1px;line-height:1}
.brand-sub{position:absolute;left:165px;top:58px;font-family:'Playfair Display',serif;color:var(--gold);font-size:11px;letter-spacing:9px}
.nav{position:absolute;top:36px;left:0;font-size:13px;color:var(--white)}
.nav a{position:absolute;color:var(--white);text-decoration:none;white-space:nowrap}
.nav a.active{color:var(--gold)}
.nav a.active::after{content:"";position:absolute;left:0;right:0;top:25px;height:1px;background:var(--gold)}
.phone-pill{position:absolute;left:891px;top:30px;width:148px;height:33px;border-radius:17px;background:var(--gold);color:var(--white);font-size:12px;display:flex;align-items:center;justify-content:center;gap:10px}
.hero-title{position:absolute;left:0;width:1200px;top:222px;text-align:center;color:var(--white);font-family:'Playfair Display',serif;font-weight:700;font-size:39px;line-height:53px}
.hero-sub{position:absolute;left:0;width:1200px;top:338px;text-align:center;color:var(--white);font-size:27px;font-weight:400;letter-spacing:1.5px}
.social-rail{position:absolute;left:1139px;top:224px;width:24px}
.social-rail span{display:block;width:22px;height:22px;border-radius:50%;border:1px solid rgba(255,255,255,.7);margin-bottom:14px}
.social-rail span.on{background:var(--gold);border-color:var(--gold)}
.scroll-line{position:absolute;left:1150px;top:335px;width:1px;height:150px;background:rgba(255,255,255,.8)}
.scroll-text{position:absolute;left:1103px;top:394px;width:110px;transform:rotate(90deg);color:var(--white);font-size:11px;text-align:center}

/* buttons */
.btn{position:absolute;height:37px;border-radius:19px;display:flex;align-items:center;font-size:14px;padding-left:24px}
.btn .knob{position:absolute;right:2px;top:2px;width:33px;height:33px;border-radius:50%;border:2px solid var(--white)}
.btn-gold{background:var(--gold);color:var(--white)}
.btn-gold .knob{background:var(--gold)}
.btn-white{background:var(--white);color:var(--ink)}
.btn-white .knob{background:var(--ink);border-color:var(--white);box-shadow:0 0 0 1px var(--ink)}

/* section headings */
.heading{position:absolute;left:0;width:1200px;text-align:center;font-family:'Playfair Display',serif;font-weight:700;font-size:34px;color:var(--ink)}
.heading em{font-style:normal;color:var(--gold)}
.rule{position:absolute;left:582px;width:36px;height:2px;background:var(--ink)}

/* about */
.about-photo{position:absolute;left:186px;top:791px;width:376px;height:376px;border-radius:50%;background:radial-gradient(circle at 45% 45%,#8f8a82,#4a4038 70%,#2e2824)}
.about-badge{position:absolute;left:441px;top:1052px;width:120px;height:120px;border-radius:50%;background:var(--gold)}
.about-text{position:absolute;left:611px;top:784px;width:426px;font-size:12.6px;line-height:21.6px;text-align:justify;color:var(--text)}

/* training */
.band-light{position:absolute;left:0;width:1200px;background:var(--light)}
.photo{position:absolute;border-radius:6px}
.sub-title{position:absolute;font-size:21px;color:var(--ink);font-weight:400}
.sub-rule{position:absolute;width:36px;height:2px;background:var(--ink)}
.body-copy{position:absolute;font-size:12.6px;line-height:21.5px;text-align:justify;color:var(--text)}

/* for sale */
.sale-bg{position:absolute;left:0;top:1968px;width:1200px;height:481px;background:linear-gradient(100deg,#5b5650 0%,#3d3b36 35%,#4b4a3f 60%,#2f2e28 100%)}
.sale-panel{position:absolute;left:251px;top:2114px;width:698px;height:260px;background:rgba(255,255,255,.12);border:1px solid rgba(255,255,255,.15)}
.sale-title{position:absolute;left:0;width:1200px;top:2128px;text-align:center;color:var(--white);font-size:22px;font-weight:500}
.sale-text{position:absolute;left:318px;top:2178px;width:566px;color:var(--white);font-size:12.4px;line-height:21.8px;text-align:justify}

/* faq */
.faq-item{position:absolute;left:224px;width:751px;background:var(--white);box-shadow:0 2px 6px rgba(0,0,0,.06);font-size:12.5px;color:var(--ink)}
.faq-head{height:44px;display:flex;align-items:center;justify-content:space-between;padding:0 16px;font-weight:500}
.faq-head .sign{color:var(--gold);font-size:16px}
.faq-item.open .faq-head{background:var(--gold);color:var(--white)}
.faq-item.open .faq-head .sign{color:var(--white)}
.faq-body{padding:14px 16px 16px;font-size:12.5px;line-height:21.5px;color:var(--ink)}

/* partnerships */
.partner-box{position:absolute;left:161px;top:3054px;width:878px;height:480px;background:linear-gradient(135deg,#cfa97c,#c59e70)}
.partner-divider{position:absolute;left:600px;top:3080px;width:1px;height:420px;background:rgba(255,255,255,.5)}
.partner-mark{position:absolute;border-radius:50%}
.partner-name{position:absolute;width:360px;text-align:center;color:var(--white);font-size:22px;font-weight:400}
.partner-rule{position:absolute;width:36px;height:2px;background:var(--white)}
.partner-text{position:absolute;width:360px;color:var(--white);font-size:12.4px;line-height:21.5px;text-align:justify}

/* footer */
.footer{position:absolute;left:0;top:3591px;width:1200px;height:447px;background:linear-gradient(90deg,#3a2a21,#4a3529 30%,#34251d 60%,#44322a 100%)}
.foot-h{position:absolute;color:var(--white);font-size:22px;font-weight:400}
.foot-rule{position:absolute;width:40px;height:2px;background:var(--gold)}
.foot-links{position:absolute;left:163px;top:3728px;list-style:none;color:var(--white);font-size:14px}
.foot-links li{height:32px;padding-left:17px;position:relative}
.foot-links li::before{content:"";position:absolute;left:2px;top:8px;width:4px;height:4px;border-radius:50%;background:var(--gold)}
.contact-row{position:absolute;left:374px;color:var(--white);font-size:14px;line-height:21px}
.contact-row .ico{position:absolute;left:0;top:4px;width:34px;height:34px;border-radius:50%;background:var(--gold-soft)}
.contact-row .txt{position:absolute;left:43px;top:0;white-space:nowrap}
.foot-brand{position:absolute;left:770px;top:3700px;width:280px;text-align:center;font-family:'Playfair Display',serif;color:var(--gold);font-size:40px;line-height:1}
.foot-brand-sub{position:absolute;left:770px;top:3750px;width:280px;text-align:center;font-family:'Playfair Display',serif;color:var(--gold);font-size:16px;letter-spacing:14px}
.follow{position:absolute;left:770px;top:3790px;width:280px;text-align:center;color:var(--white);font-size:21px}
.foot-social span{position:absolute;top:3831px;width:32px;height:32px;border-radius:50%;background:var(--gold-soft)}
.copyright{position:absolute;left:0;width:1200px;top:4006px;text-align:center;color:var(--white);font-size:13px}
</style>
</head>
<body>

<!-- header / hero -->
<svg class="hero-bg" viewBox="0 0 1200 660" role="img" aria-label="Jockey in racing silks galloping a bay horse along a white rail">
  <defs>
    <linearGradient id="heroGrad" x1="0" y1="0" x2="1" y2="1">
      <stop offset="0" stop-color="#6a6e5c"/>
      <stop offset=".45" stop-color="#5b4430"/>
      <stop offset="1" stop-color="#7a7650"/>
    </linearGradient>
  </defs>
  <path d="M0 0H1200V500Q600 740 0 500Z" fill="url(#heroGrad)"/>
  <path d="M0 0H1200V500Q600 740 0 500Z" fill="rgba(0,0,0,.25)"/>
</svg>

<div class="brand">LINDEN RIDGE</div>
<div class="brand-sub">STABLES</div>

<nav class="nav">
  <a class="active" style="left:409px">Home</a>
  <a style="left:476px">About Us</a>
  <a style="left:564px">Services</a>
  <a style="left:647px">News Room</a>
  <a style="left:752px">Blog</a>
  <a style="left:811px">Contact</a>
</nav>
<div class="phone-pill">
  <svg width="14" height="14" viewBox="0 0 24 24"><path d="M6.6 10.8a15 15 0 0 0 6.6 6.6l2.2-2.2a1 1 0 0 1 1-.25 11.4 11.4 0 0 0 3.6.6 1 1 0 0 1 1 1V20a1 1 0 0 1-1 1A17 17 0 0 1 3 4a1 1 0 0 1 1-1h3.5a1 1 0 0 1 1 1c0 1.25.2 2.45.6 3.6a1 1 0 0 1-.25 1z" fill="none" stroke="#fff" stroke-width="2"/></svg>
  555-014-2280
</div>

<h1 class="hero-title">Central Iowa’s Premier<br>Dressage And Sport Horse Training</h1>
<p class="hero-sub">Located Outside Des Moines, Iowa</p>
<div class="btn btn-white" style="left:454px;top:394px;width:146px">Services<span class="knob"></span></div>
<div class="btn btn-gold" style="left:616px;top:394px;width:146px">Contact Us<span class="knob"></span></div>

<div class="social-rail"><span></span><span class="on"></span><span></span></div>
<div class="scroll-line"></div>
<div class="scroll-text">Scroll Down</div>

<div class="abs" style="left:555px;top:555px;width:90px;height:90px;border-radius:50%;background:var(--ink);border:4px solid var(--white)"></div>

<!-- about -->
<h2 class="heading" style="top:702px"><em>About</em> Us</h2>
<div class="rule" style="top:757px"></div>
<div class="about-photo" role="img" aria-label="Rider in show attire on a dark dressage horse in an indoor arena"></div>
<div class="about-badge"></div>
<p class="about-text">Upper-Level Rider And Trainer, Clara Whitfield Began Her Riding Career At A Young Age. She Went Up Through The Ranks Of Youth Riding Club And With An Emphasis And Focus In Eventing. During College, Clara Worked For A Small Breeder Starting Young Horses. Clara Loves Starting Young Horses Including Starting And Guiding Them In A Correct And Quiet Way To Help Them Flourish. Her Training Focuses On Gymnastic Training Incorporating Ground Work/lunging/long Lining, Jumping, Cavelletti And Regular Hacking And Trail Riding. Clara Is A National Federation Silver Medalist Having Competed Through The Upper Levels Of It. A Learner At Heart, Clara Regularly Clinics And Rides With Other Trainers And Accomplished Dressage Riders From Across The Nation To Continue To Pursue Her Goal Of Competing At The Grand Prix. Clara has attended the federation L Program as well as the Instructor/Trainer program to continue her growth as a trainer and rider.</p>
<div class="btn btn-gold" style="left:612px;top:1133px;width:149px">Read More<span class="knob"></span></div>

<!-- training & lessons -->
<div class="band-light" style="top:1266px;height:702px"></div>
<h2 class="heading" style="top:1322px"><em>Training</em> &amp; Lessons</h2>
<div class="rule" style="top:1377px"></div>

<div class="photo" style="left:193px;top:1408px;width:379px;height:226px;background:linear-gradient(135deg,#6f8a52,#6a5240 50%,#9a9690)" role="img" aria-label="Rider trotting a bay horse in lavender boots over poles"></div>
<h3 class="sub-title" style="left:619px;top:1404px">Training</h3>
<div class="sub-rule" style="left:619px;top:1440px"></div>
<p class="body-copy" style="left:621px;top:1465px;width:330px">Linden Ridge Stables Offers Both Full And Half Time Training Options With Clara Whitfield. There Is Much Flexibility With Both Rides And/or Lessons Weekly In The Training Packages...</p>
<div class="btn btn-gold" style="left:627px;top:1575px;width:146px">Read More<span class="knob"></span></div>

<h3 class="sub-title" style="left:440px;width:132px;text-align:right;top:1664px">Lessons</h3>
<div class="sub-rule" style="left:536px;top:1700px"></div>
<p class="body-copy" style="left:240px;top:1725px;width:332px">Lessons are available for all ages of riders. Clara thoroughly enjoys working with accomplished riders looking to succeed in the show ring, as well as riders...</p>
<div class="btn btn-gold" style="left:426px;top:1814px;width:146px">Read More<span class="knob"></span></div>
<div class="photo" style="left:620px;top:1667px;width:380px;height:224px;background:linear-gradient(135deg,#8a7a6a,#d9d4cc 45%,#b08a76)" role="img" aria-label="Rider on a bay horse beside an arena fence with mountains behind"></div>

<!-- for sale -->
<div class="sale-bg" role="img" aria-label="Grey horses grazing in a fenced paddock at dusk"></div>
<h2 class="heading" style="top:2024px;color:var(--white)">For Sale</h2>
<div class="rule" style="top:2078px;background:var(--white)"></div>
<div class="sale-panel"></div>
<h3 class="sale-title">Silver Cadence</h3>
<p class="sale-text">Silver Cadence, “Cade,” (Corvan x Northern Pilot) is a 2012, 16hh imported Hanoverian. Cade is an incredibly quiet and kind horse. He is ridden by both an amatuer and child rider. He loves to hack and is very quiet alone and with a group of horses. He has shown through first level with scores into the 70’s at both training and first level. Cade is currently solidly schooling all of second level, as well as half passes and flying changes from third level. Cade has 3 very easy to ride gaits and it is easy for riders to sit his trot. Very quiet and well mannered on the ground with vet, farrier and clipping. He has lovely confirmation with a striking head. He is regularly admired at shows! Cade is very versatile and game and also loves to jump!</p>

<!-- faq -->
<div class="band-light" style="top:2449px;height:461px"></div>
<h2 class="heading" style="top:2510px"><em>Frequently</em> Asked Questions</h2>
<div class="rule" style="top:2564px"></div>
<div class="faq-item open" style="top:2595px">
  <div class="faq-head"><span>Lorem Ipsum</span><span class="sign">–</span></div>
  <div class="faq-body">Lorem Ipsum is simply dummy text of the printing and typesetting industry. Lorem Ipsum has been the industry’s standard dummy text ever since the 1500s, when an unknown printer took a galley of type.</div>
</div>
<div class="faq-item" style="top:2728px"><div class="faq-head"><span>Lorem Ipsum Dolor Sit Amet</span><span class="sign">+</span></div></div>
<div class="faq-item" style="top:2795px"><div class="faq-head"><span>Lorem Ipsum</span><span class="sign">+</span></div></div>

<!-- partnerships -->
<h2 class="heading" style="top:2967px">Partnerships</h2>
<div class="rule" style="top:3022px"></div>
<div class="partner-box"></div>
<div class="partner-divider"></div>

<div class="partner-mark" style="left:334px;top:3083px;width:42px;height:42px;background:#8a2a22"></div>
<h3 class="partner-name" style="left:195px;top:3176px">Fairmont Saddlery</h3>
<div class="partner-rule" style="left:357px;top:3219px"></div>
<p class="partner-text" style="left:195px;top:3244px">Fairmont Saddlery is constantly designing and researching saddles and riders to find the right blend of design and craftsmanship to fit today’s demands. Every saddle’s detail is carefully checked to be sure the workmanship and quality is there. All saddles are anatomically designed for horse and rider, hand-crafted from the finest leathers, and manufactured using the most technically advanced methods and features available.</p>
<div class="btn btn-white" style="left:308px;top:3442px;width:146px">Read More<span class="knob"></span></div>

<div class="partner-mark" style="left:805px;top:3083px;width:42px;height:42px;background:#4a4a4a"></div>
<h3 class="partner-name" style="left:645px;top:3176px">Harwell’s Saddlery</h3>
<div class="partner-rule" style="left:807px;top:3219px"></div>
<p class="partner-text" style="left:645px;top:3244px">My goal is to provide the best possible fit for both horse and rider whether it is a saddle you already own, one you have on trial, or one that I carry. Being a Qualified Saddle Fitter by the Guild of Saddle Fitters allows me to work with all saddle types and brands. In addition, I carry a broad range of saddles to fit your needs, both new and used. Having a multitude of saddles in my stock makes saddle shopping much easier for you.</p>
<div class="btn btn-white" style="left:746px;top:3442px;width:146px">Read More<span class="knob"></span></div>

<!-- footer -->
<footer class="footer" role="img" aria-label="Dark stained wood plank texture"></footer>
<h4 class="foot-h" style="left:163px;top:3667px">Quick Links</h4>
<div class="foot-rule" style="left:163px;top:3708px"></div>
<ul class="foot-links">
  <li>HOME</li><li>ABOUT US</li><li>SERVICES</li><li>LATEST NEWS</li><li>BLOG</li><li>CONTACT</li>
</ul>

<h4 class="foot-h" style="left:374px;top:3667px">Contact Details</h4>
<div class="foot-rule" style="left:374px;top:3708px"></div>
<div class="contact-row" style="top:3731px">
  <span class="ico"><svg width="34" height="34" viewBox="0 0 34 34"><path d="M17 9a5.5 5.5 0 0 0-5.5 5.5C11.5 19 17 25 17 25s5.5-6 5.5-10.5A5.5 5.5 0 0 0 17 9z" fill="#fff"/><circle cx="17" cy="14.5" r="2" fill="#c9a57a"/></svg></span>
  <span class="txt">Address<br>4820 Meadow Lane, Ashford Center, IA 50999</span>
</div>
<div class="contact-row" style="top:3800px">
  <span class="ico"><svg width="34" height="34" viewBox="0 0 34 34"><path d="M12.5 15.5a12 12 0 0 0 6 6l2-2a.8.8 0 0 1 .8-.2 9 9 0 0 0 2.8.5.8.8 0 0 1 .8.8V24a.8.8 0 0 1-.8.8A13.6 13.6 0 0 1 9.2 11a.8.8 0 0 1 .8-.8h3.2a.8.8 0 0 1 .8.8c0 1 .2 2 .5 2.8a.8.8 0 0 1-.2.8z" fill="#fff"/></svg></span>
  <span class="txt">Phone<br>555-014-2280</span>
</div>
<div class="contact-row" style="top:3869px">
  <span class="ico"><svg width="34" height="34" viewBox="0 0 34 34"><rect x="10" y="12" width="14" height="10" rx="1" fill="#fff"/><path d="M10 12.5l7 5 7-5" fill="none" stroke="#c9a57a" stroke-width="1.3"/></svg></span>
  <span class="txt">EMAIL<br>clara.whitfield@lindenridgestables.com</span>
</div>

<div class="foot-brand">LINDEN RIDGE</div>
<div class="foot-brand-sub">STABLES</div>
<div class="follow">Follow Us</div>
<div class="foot-social">
  <span style="left:827px"></span><span style="left:877px"></span><span style="left:926px"></span><span style="left:976px"></span>
</div>
<p class="copyright">Copyright © 2021 LINDEN RIDGE STABLES. All Rights Reserved.</p>

</body>
</html>
```